Contemporary update for a market leader in foodservice distribution

KORLO is a market leader in foodservice distribution nationwide.
We have recently adopted a new look and feel for our flagship foodservice rewards programme, and we're looking to have our business cards reflect our new aesthetic. Below is a link to our new rewards website to give you a general idea on the look we're after. https://korlotierclub.com.au/

Industry/Entity Type

Distribution

Contact Information for Business Card

Must have space for contact name, position, company name and ABN, address, phone number and direct number, fax, email, and web address.

Font styles to use
Serif
Sans Serif

Requirements
Must have
• We'd like a landscape design, with our 'Bright Ember Tier' logo incorporated on either the front or the back of the card. The overall design should be contemporary and professional.
Nice to have
• I have included both the full colour and white version of our company logo - our preference is to have the company logo one solid colour (white, or a shade of grey) although we're also open to designs including the full colour logo. If you are able to incorporate a small Chatterleaf and Workmesh logo, please do so.
Should not have
• Should not have an over-complicated design. No images of globes, or food.

```html
<!DOCTYPE html>
<html lang="en">
<head>
<meta charset="utf-8">
<title>Bright Ember Tier – Business Cards</title>
<link rel="stylesheet" href="https://fonts.googleapis.com/css2?family=Open+Sans:wght@400;600;800&display=swap">
<style>
  :root {
    --backdrop: #e9e6e1;
    --card-black: #050505;
    --card-sheen: #1c1c1c;
    --ink-white: #ffffff;
    --ink-soft: #d9d9d9;
    --accent-green: #2fb463;
  }
  * { margin: 0; padding: 0; box-sizing: border-box; }
  html, body {
    width: 1200px;
    height: 902px;
    overflow: hidden;
    background: var(--backdrop);
    font-family: "Open Sans", Arial, sans-serif;
  }
  .canvas {
    position: relative;
    width: 1200px;
    height: 902px;
  }
  .card {
    position: absolute;
    width: 580px;
    height: 331px;
    background: linear-gradient(125deg, var(--card-sheen) 0%, var(--card-black) 45%, var(--card-black) 100%);
    color: var(--ink-white);
    box-shadow: 0 14px 30px rgba(0,0,0,0.28);
    display: flex;
    flex-direction: column;
    align-items: center;
  }
  .card--front { left: 140px; top: 70px; padding-top: 48px; }
  .card--back  { left: 480px; top: 500px; justify-content: center; }

  .brand {
    display: flex;
    flex-direction: column;
    align-items: center;
  }
  .brand__row {
    display: flex;
    align-items: center;
    gap: 10px;
  }
  .brand__dot {
    width: 22px;
    height: 22px;
    border-radius: 50%;
    background: var(--accent-green);
  }
  .brand__name {
    font-weight: 800;
    font-size: 30px;
    letter-spacing: 0.5px;
    line-height: 1;
  }
  .brand__tagline {
    margin-top: 6px;
    font-weight: 600;
    font-size: 7px;
    letter-spacing: 1.2px;
    text-transform: uppercase;
  }
  .card--back .brand__name { font-size: 40px; }
  .card--back .brand__dot { width: 28px; height: 28px; }
  .card--back .brand__tagline { font-size: 9px; margin-top: 8px; }

  .contact-name {
    margin-top: 30px;
    font-size: 17px;
    font-weight: 400;
    text-transform: uppercase;
    letter-spacing: 0.3px;
  }
  .contact-role {
    font-size: 10px;
    text-transform: uppercase;
    color: var(--ink-soft);
    letter-spacing: 0.5px;
  }
  .contact-address {
    margin-top: 40px;
    font-size: 12px;
  }
  .contact-lines {
    margin-top: 10px;
    font-size: 13px;
    word-spacing: 1px;
  }
  .contact-lines .divider { margin: 0 8px; }
</style>
</head>
<body>
<main class="canvas">
  <section class="card card--front" aria-label="Business card front">
    <div class="brand">
      <div class="brand__row">
        <span class="brand__name">Bright Ember Tier</span>
        <span class="brand__dot"></span>
      </div>
      <span class="brand__tagline">Foodservice Rewards</span>
    </div>
    <p class="contact-name">Person Name</p>
    <p class="contact-role">Designation</p>
    <p class="contact-address">Consectetur adipiscing elit, Donec accumsan.</p>
    <p class="contact-lines">P: 123 456 7890<span class="divider">|</span>F: 123 456 7890<span class="divider">|</span>E: info@abcdefg.com</p>
  </section>

  <section class="card card--back" aria-label="Business card back">
    <div class="brand">
      <div class="brand__row">
        <span class="brand__name">Bright Ember Tier</span>
        <span class="brand__dot"></span>
      </div>
      <span class="brand__tagline">Foodservice Rewards</span>
    </div>
  </section>
</main>
</body>
</html>
```